Local Flower Farm Needs Business Card Design

I need business cards designed for a flower farm based in Eudora, Kansas.
Business Info:
We are a local cut flower farm located in Eudora, Kansas, founded by Darla Whitcombe. What started as a passion for agriculture and search for more joy in daily life has blossomed into a small business dedicated to providing the community with beautiful, fresh, and sustainable flowers. We specialize in local, seasonal blooms, ensuring that every petal reflects the care and dedication we pour into our craft. Our mission is to deliver the highest quality flowers directly to our customers through local farmers markets and to florists who share our commitment to sustainability. Join us in celebrating the beauty of nature, one bloom at a time!
Contact Details:
Darla Whitcombe
Owner
Phone 913-555-0148
Facebook: Rosalind Pike Gardens
Instagram: @RosalindPikeGardens
Website: RosalindPikeGardens.example
Target Market(s)
Wholesale to Florists and Direct to Consumer via Farmers Market
Industry/Entity Type
Florist, Farm
Contact Information for Business Card
Name, Contact Info, Logo
Look and feel
Each slider illustrates characteristics of the customer's brand and the style your logo design should communicate.

```html
<!DOCTYPE html>
<html lang="en">
<head>
<meta charset="utf-8">
<title>Rosalind Pike Gardens – Business Card</title>
<link rel="stylesheet" href="https://fonts.googleapis.com/css2?family=Bodoni+Moda:wght@400;500&display=swap">
<style>
  :root {
    --backdrop: #e6e6e4;
    --card: #ffffff;
    --ink: #13302b;
    --text: #2a2a2a;
    --rule: #6b6b6b;
  }
  * { margin: 0; padding: 0; box-sizing: border-box; }
  html, body { width: 1200px; height: 900px; overflow: hidden; }
  body {
    background: var(--backdrop);
    font-family: "Bodoni Moda", "Times New Roman", serif;
    position: relative;
  }
  .card {
    position: absolute;
    top: 302px;
    width: 515px;
    height: 296px;
    background: var(--card);
    box-shadow: 0 2px 6px rgba(0,0,0,0.18);
  }
  .card--front { left: 72px; }
  .card--back { left: 615px; }

  /* Front */
  .badge {
    position: absolute;
    left: 50%; top: 50%;
    width: 222px; height: 222px;
    transform: translate(-50%, -50%);
    border: 1px solid var(--ink);
    border-radius: 50%;
    display: flex;
    align-items: center;
    justify-content: center;
    text-align: center;
  }
  .badge__name {
    color: var(--ink);
    font-size: 25px;
    font-weight: 500;
    line-height: 1.15;
    letter-spacing: 0.06em;
    text-transform: uppercase;
  }

  /* Back */
  .brand-name {
    position: absolute;
    left: 36px; top: 0; bottom: 0;
    width: 170px;
    display: flex;
    align-items: center;
    justify-content: center;
    text-align: center;
    color: var(--ink);
    font-size: 27px;
    font-weight: 500;
    line-height: 1.1;
    letter-spacing: 0.03em;
    text-transform: uppercase;
  }
  .divider {
    position: absolute;
    left: 225px; top: 40px;
    width: 1px; height: 224px;
    background: var(--rule);
  }
  .contact {
    position: absolute;
    left: 250px; top: 72px;
    color: var(--text);
    font-size: 13.5px;
    list-style: none;
  }
  .contact__name {
    font-size: 17px;
    letter-spacing: 0.04em;
    text-transform: uppercase;
    line-height: 1.1;
  }
  .contact__role {
    font-size: 13px;
    letter-spacing: 0.06em;
    text-transform: uppercase;
    margin-top: 4px;
    margin-bottom: 20px;
  }
  .contact__line {
    display: flex;
    align-items: center;
    gap: 5px;
    line-height: 1.5;
  }
  .contact__line--gap { margin-top: 8px; }
  .contact__icon { width: 10px; height: 10px; flex: none; }
  .contact__dot {
    width: 8px; height: 8px; flex: none;
    border-radius: 50%;
    background: var(--text);
    margin: 0 1px;
  }
</style>
</head>
<body>
  <section class="card card--front" aria-label="Card front">
    <div class="badge">
      <span class="badge__name">Rosalind<br>Pike<br>Gardens</span>
    </div>
  </section>

  <section class="card card--back" aria-label="Card back">
    <div class="brand-name">Rosalind Pike Gardens</div>
    <div class="divider"></div>
    <div class="contact">
      <div class="contact__name">Darla Whitcombe</div>
      <div class="contact__role">Owner</div>
      <div class="contact__line">
        <svg class="contact__icon" viewBox="0 0 10 10" aria-hidden="true">
          <path d="M1 3.5 Q5 0.5 9 3.5 L8 5 L6.5 4.2 L6.5 3.4 Q5 2.9 3.5 3.4 L3.5 4.2 L2 5 Z" fill="#2a2a2a"/>
          <rect x="2.5" y="5" width="5" height="3.5" rx="0.6" fill="#2a2a2a"/>
        </svg>
        <span>913-555-0148</span>
      </div>
      <div class="contact__line contact__line--gap">
        <span class="contact__dot" aria-hidden="true"></span>
        <span>Rosalind Pike Gardens</span>
      </div>
      <div class="contact__line">
        <span class="contact__dot" aria-hidden="true"></span>
        <span>@RosalindPikeGardens</span>
      </div>
      <div class="contact__line contact__line--gap">
        <svg class="contact__icon" viewBox="0 0 10 10" aria-hidden="true">
          <circle cx="5" cy="5" r="4.3" fill="none" stroke="#2a2a2a" stroke-width="1"/>
          <ellipse cx="5" cy="5" rx="1.8" ry="4.3" fill="none" stroke="#2a2a2a" stroke-width="0.8"/>
          <line x1="0.7" y1="5" x2="9.3" y2="5" stroke="#2a2a2a" stroke-width="0.8"/>
        </svg>
        <span>RosalindPikeGardens.example</span>
      </div>
    </div>
  </section>
</body>
</html>
```